Vision, Mission and Culture Posters

We have written text paragraphs for our company vision and mission and need them made into a2 or a3 sized posters using our logo for inspiration for colour. Our company culture has 10 paragraphs and we'd like this to be a single poster of a2 or a1. Each poster should have the logo on and share common design. It's not a complex job really.

Industry/Entity Type

It Company

Requirements
Nice to have
• These will be going up on our office wall so need to be clear to read from a distance and look professional but also not stodgy.

```html
<!DOCTYPE html>
<html lang="en">
<head>
<meta charset="utf-8">
<title>Kerbside Bay Rentals – Company Values</title>
<link href="https://fonts.googleapis.com/css2?family=Open+Sans:wght@700;800&family=PT+Sans+Narrow:wght@400&display=swap" rel="stylesheet">
<style>
  :root {
    --cream-light: #fffef2;
    --cream: #fbf6cf;
    --brand-yellow: #fff200;
    --ink: #111111;
    --band: #000000;
    --value-red: #e8262b;
    --number-grey: #8f8f8f;
    --deco-navy: #1a3f86;
    --deco-sky: #a9dcef;
    --white: #ffffff;
  }
  * { margin: 0; padding: 0; box-sizing: border-box; }
  html, body { width: 848px; height: 1200px; overflow: hidden; }
  body { background: var(--white); }

  .poster {
    position: relative;
    width: 848px;
    height: 1200px;
    overflow: hidden;
    background: radial-gradient(ellipse at 50% 55%, var(--cream-light) 0%, var(--cream) 80%);
  }

  .masthead {
    position: absolute; left: 0; top: 0; width: 848px; height: 220px;
    background: var(--white);
  }
  .brand-panel {
    position: absolute; left: 119px; top: 22px; width: 606px; height: 180px;
    background: var(--brand-yellow);
    border-radius: 16px;
    display: flex; align-items: center; justify-content: center; gap: 24px;
  }
  .brand-mark { width: 34px; height: 34px; background: var(--value-red); flex: none; }
  .brand-name {
    font-family: "Open Sans", sans-serif;
    font-weight: 700;
    font-size: 46px;
    line-height: 1.1;
    color: var(--ink);
    letter-spacing: 1px;
  }

  .title-band {
    position: absolute; left: 0; top: 219px; width: 848px; height: 77px;
    background: var(--band);
    display: flex; align-items: center; justify-content: center;
  }
  .title-band h1 {
    font-family: "Open Sans", sans-serif;
    font-weight: 700;
    font-size: 33px;
    color: var(--white);
  }

  .footer-decoration {
    position: absolute; left: 0; top: 1000px; width: 848px; height: 200px;
    background: linear-gradient(to top right,
      var(--deco-navy) 0%, var(--deco-navy) 22%,
      var(--deco-sky) 42%, rgba(169, 220, 239, 0.35) 62%, rgba(251, 246, 207, 0) 80%);
  }

  .value { position: absolute; }
  .value-head { display: flex; align-items: baseline; gap: 14px; height: 46px; }
  .value-number {
    font-family: "Open Sans", sans-serif;
    font-weight: 800;
    font-size: 50px;
    line-height: 46px;
    color: var(--number-grey);
  }
  .value-title {
    font-family: "Open Sans", sans-serif;
    font-weight: 700;
    font-size: 33px;
    line-height: 46px;
    color: var(--value-red);
    white-space: nowrap;
  }
  .value-text {
    font-family: "PT Sans Narrow", sans-serif;
    font-size: 14.2px;
    line-height: 17px;
    color: var(--ink);
    hyphens: auto;
  }
  .col-left { left: 22px; }
  .col-right { left: 460px; }
  .col-left .value-text { margin-left: 34px; width: 382px; }
  .col-right .value-text { margin-left: 33px; width: 330px; }
</style>
</head>
<body>
<main class="poster">
  <header class="masthead">
    <div class="brand-panel">
      <span class="brand-mark"></span>
      <span class="brand-name">Kerbside Bay Rentals</span>
    </div>
  </header>

  <div class="title-band"><h1>Company Values</h1></div>

  <div class="footer-decoration" role="img" aria-label="Decorative navy, sky blue and lime green wave swooshes along the bottom of the poster"></div>

  <section class="value col-left" style="top:314px">
    <div class="value-head"><span class="value-number">1</span><h2 class="value-title">Communication</h2></div>
    <p class="value-text">We believe in open communication providing our customers, colleagues and others with honest, accurate, concise and prompt information relevant to their needs to ensure everyone always has a sound understanding of any matter being communicated. We are polite, friendly and warm and we use good communication as a means of enhancing our customer experience.</p>
  </section>

  <section class="value col-left" style="top:452px">
    <div class="value-head"><span class="value-number">2</span><h2 class="value-title">Education</h2></div>
    <p class="value-text">We believe in the importance of continual learning and education and thrive on helping our colleagues by sharing our knowledge and learnings. We learn from our mistakes and use them to build a better, stronger, closer team environment. Understanding that everyone's needs are different and that we learn in different ways, we challenge our people to constantly improve their professional development in a way that works best for them.</p>
  </section>

  <section class="value col-left" style="top:610px">
    <div class="value-head"><span class="value-number">3</span><h2 class="value-title">Professionalism</h2></div>
    <p class="value-text">We represent ourselves as professionals and our business to the best of our abilities at all times taking particular care to give the best impression of ourselves to those we interact with during the course of our working days whether that be by phone, email or in person. We are always on time, well presented, well prepared and work hard to succeed.</p>
  </section>

  <section class="value col-left" style="top:748px">
    <div class="value-head"><span class="value-number">4</span><h2 class="value-title">Ownership</h2></div>
    <p class="value-text">We are each fully responsible for our roles and for our contribution to the success of our business. We are accountable for our results, our ability to improve at what we do, our mistakes and what we do to correct them.</p>
  </section>

  <section class="value col-left" style="top:852px">
    <div class="value-head"><span class="value-number">5</span><h2 class="value-title">CommercialAwareness</h2></div>
    <p class="value-text">We understand that in a small business everything we do can impact the success of our business and we commit ourselves to thinking about the impact on our business of all the decisions we make before we make them. We consider cost against benefit, remembering the cheapest option doesn't always give the greatest benefit, the best value use of our time, who benefits from what we do and how it benefits our business.</p>
  </section>

  <section class="value col-right" style="top:314px">
    <div class="value-head"><span class="value-number">6</span><h2 class="value-title">Balance</h2></div>
    <p class="value-text">We try to find the best balance in our lives between our responsibilities, obligations, duties and desires whilst still ensuring we have time to devote to friends, families, fun and life. We try to balance our opinions and thoughts with those of others and believe that with balance comes fairness, integrity, self-control and a great attitude.</p>
  </section>

  <section class="value col-right" style="top:484px">
    <div class="value-head"><span class="value-number">7</span><h2 class="value-title">Customer Service</h2></div>
    <p class="value-text">We believe that without our customers we would not be successful and understand the outstanding level of service we give them is critical to our continued success, even down to the smallest action whenever that may be required from us. We go out of our way to help any customer with an issue and are only satisfied when we have helped them achieve a fair outcome they are happy with.</p>
  </section>

  <section class="value col-right" style="top:662px">
    <div class="value-head"><span class="value-number">8</span><h2 class="value-title">Consistency</h2></div>
    <p class="value-text">We believe in consistency of our work, our approach, our positive attitude and our actions to set a standard at which our colleagues and customers feel a level of familiarity that strengthens our relationship whilst representing ourselves and our business to their best.</p>
  </section>

  <section class="value col-right" style="top:802px">
    <div class="value-head"><span class="value-number">9</span><h2 class="value-title">Success</h2></div>
    <p class="value-text">We understand success isn't given, it is earned every day, piece by piece. We are driven to succeed as an individual and as a team and we support each other in earning that success. We are not afraid to celebrate our successes to acknowledge our hard work and dedication to our achieving our goals.</p>
  </section>

  <section class="value col-right" style="top:942px">
    <div class="value-head"><span class="value-number">10</span><h2 class="value-title">Commitment</h2></div>
    <p class="value-text">We are committed to the company vision, the mission and to upholding the company culture as well as showing the company the same commitment it has shown to us. We talk about our vision, mission and culture often, use them to help guide ourselves and our colleagues as we go about our work. We are not afraid to let our colleagues know when we feel they are not showing the right commitment to our vision, mission and culture but make sure we do so in a positive and helpful way to ensure they can get back on track as easily as possible.</p>
  </section>
</main>
</body>
</html>
```